Design for a Service-Based Estimate

We want a design for an Estimate that will always be sent in PDF format. The estimate or proposal is a critical document that needs to plainly show the service items, item description but also needs to be attractive and professional looking. Our current estimate deliverable is attached but it looks really basic like a Word document

```html
<!DOCTYPE html>
<html lang="en">
<head>
<meta charset="utf-8">
<title>Estimate – Keystone Slab</title>
<link href="https://fonts.googleapis.com/css2?family=Open+Sans:wght@400;600;700;800&display=swap" rel="stylesheet">
<style>
:root{
  --red:#d4472b;
  --navy:#2f3150;
  --grey-row:#e3e3e3;
  --text:#3a3a3a;
  --muted:#6d6d6d;
  --bg:#dcdcdc;
  --peach:#f3d3c3;
}
*{box-sizing:border-box;margin:0;padding:0}
html,body{width:1200px;height:1200px;overflow:hidden}
body{background:var(--bg);font-family:"Open Sans",Arial,sans-serif;color:var(--text);display:flex;align-items:center;justify-content:center}
.page{width:840px;height:1140px;background:linear-gradient(180deg,#fff 0%,#fff 60%,var(--peach) 100%);position:relative;padding:60px 56px;box-shadow:0 4px 18px rgba(0,0,0,.12)}
.header{display:flex;justify-content:space-between;align-items:flex-start}
.brand{margin-top:120px;display:flex;align-items:center;gap:10px}
.brand-mark{width:16px;height:16px;background:var(--red)}
.brand-name{font-weight:800;font-size:30px;letter-spacing:2px;color:var(--navy);text-transform:uppercase}
.doc-title{text-align:right}
.badge{display:inline-block;background:var(--red);color:#fff;font-weight:700;font-size:50px;letter-spacing:2px;padding:6px 40px;border-radius:30px 0 30px 0}
.project{margin-top:16px;font-weight:700;font-size:16px;color:#555;line-height:1.4;text-transform:uppercase;padding-right:10px}
.client{margin-top:28px;font-size:13px;line-height:1.6}
.client .label{color:var(--red)}
.table{margin-top:26px}
.thead{display:grid;grid-template-columns:1fr 100px 70px 100px 110px;gap:8px}
.pill{background:var(--red);color:#fff;font-weight:600;font-size:14px;padding:6px 14px;border-radius:14px 0 14px 0;text-align:center}
.pill.item{text-align:left}
.row{display:grid;grid-template-columns:1fr 100px 70px 100px 110px;gap:8px;background:var(--grey-row);margin-top:8px;padding:10px 14px;font-size:11.5px;line-height:1.5}
.row .num{text-align:center;align-self:center}
.row .money{text-align:right;align-self:center}
.totals{display:flex;justify-content:flex-end;gap:12px;margin-top:18px}
.total-label,.total-value{background:var(--navy);color:#fff;font-weight:700;border-radius:14px 0 14px 0;padding:8px 22px}
.total-label{font-size:15px}
.total-value{font-size:20px}
.rule{height:1px;background:#b9b9c4;margin-top:20px}
.terms-title{margin-top:36px;color:var(--red);font-weight:700;font-size:16px}
.terms-rule{width:220px;height:1px;background:var(--navy);margin-top:6px}
.terms{margin-top:16px;padding-left:18px;font-size:11.5px;line-height:1.7}
.signs{display:flex;justify-content:space-between;margin-top:60px;font-size:14px}
.sign{width:300px}
.sign .line{border-bottom:1.5px dotted #555;height:40px}
</style>
</head>
<body>
<main class="page">
  <header class="header">
    <div>
      <div class="brand"><span class="brand-mark"></span><span class="brand-name">Keystone Slab</span></div>
      <div class="client">
        <div>To:</div>
        <div>Dale Morrow,</div>
        <div><span class="label">E:</span> dmorrow@example.com</div>
        <div>482 Harbor Lane SW Fairview 30412</div>
        <div>Bid#: 20 - 01812</div>
      </div>
    </div>
    <div class="doc-title">
      <div class="badge">INVOICE</div>
      <div class="project">Dale Morrow<br>New Concrete Pad</div>
    </div>
  </header>

  <section class="table">
    <div class="thead">
      <div class="pill item">Item</div>
      <div class="pill">Quantity</div>
      <div class="pill">U/M</div>
      <div class="pill">Unit $</div>
      <div class="pill">Total $</div>
    </div>
    <div class="row">
      <div>Form, Pour &amp; finish New Concrete Slab (24' X 24' X4")<br>Includes: 3000psi Concrete Mix, Footer (12" X 8")<br>with One (#5) Continuous Reber, Wire Mesh<br>Reinforcement and Saw-Cut Expansion Joints.</div>
      <div class="num">576</div><div class="num">SF</div><div class="money">$ 8.65</div><div class="money">$ 4,982.40</div>
    </div>
    <div class="row">
      <div>Optional : Add ( 2' X 24' X 4" ) Small Ramp Area</div>
      <div class="num">48</div><div class="num">SF</div><div class="money">$ 8.65</div><div class="money">$ 415.20</div>
    </div>
    <div class="totals">
      <div class="total-label">TOTAL PRICE</div>
      <div class="total-value">$ 5,397.60</div>
    </div>
    <div class="rule"></div>
  </section>

  <section>
    <h2 class="terms-title">TERMS &amp; CONDITIONS</h2>
    <div class="terms-rule"></div>
    <ol class="terms">
      <li>Prices as quoted in this estimate are valid for 60 Days only.</li>
      <li>Payment in full, less any previously paid amounts, is due to the contractor upon completion of the proposed scope of work.</li>
      <li>All change order requets must be communicated in writing to the contractor by the client or their authorized representative.</li>
      <li>All the mesurement listed in this estimate are aproximate and may vary due to actual field condition.</li>
      <li>It is agreed by the contractor and the client that complications and costs arising fom unforeseen condition and handling of unsuitable materials are not included in this estimate.</li>
      <li>Unless specifically listed in this estimate, the following items and their are not included: Maintenance of Traffic, Concrete Material pumping, Testing, Excavation, Grading and fill Material, permits and Fees, Surveying and As-builts, Irrigation Repair, Landscping and root Mitigation, De-watering, Private Locates and Accessibility.</li>
      <li>Private utility locating seervices using radio devices and, when necessary, ground penetration radar are offered by Keystone Slab to assist finding private utilities that may not have been lacated by the public one call system. Keystone Slab will not be responsible for private utilities that may not have been lacated nor for the failure of the above equipment to accurately detect existing utilities since the equipment is fallible and existing site conditions may preclude the ability of the equipment to detect an identifiable signal.</li>
    </ol>
  </section>

  <footer class="signs">
    <div class="sign">Client Signature<div class="line"></div></div>
    <div class="sign">Date<div class="line"></div></div>
  </footer>
</main>
</body>
</html>
```